Tail Wags Corner

We need a sign design for our new Pet store in Dublin Ireland
The sign has also room for a banner underneath the sign which we feel should show the basic categories of animals we cater for.
Aquatic,Bird,Cat,Dog, small animal and reptile.
I would like these categories in a similar design to Tablix app for example in bright colours with maybe silhouette of animal inside.
We would then incorporate these individual APPs within the category inside the store
the shop name should be blend well the idea above but Tail Wag Corner should not be complicated I feel
70% female and children
Store

```html
<!DOCTYPE html>
<html lang="en">
<head>
<meta charset="utf-8">
<title>Tail Wag Corner – Store Sign</title>
<link rel="stylesheet" href="https://fonts.googleapis.com/css2?family=Comfortaa:wght@300;400&display=swap">
<style>
  :root {
    --sign-black: #000000;
    --gap-white: #ffffff;
    --name-orange: #ff7a10;
    --tagline-cyan: #22e6f0;
    --rule-white: #ffffff;
    --label-white: #ffffff;
    --fish-a: #ff8a00; --fish-b: #ffe600;
    --bird-a: #1020e0; --bird-b: #20d8ff;
    --cat-a: #f01a00;  --cat-b: #ff9a00;
    --dog-a: #0d5a00;  --dog-b: #55e020;
    --small-a: #6a0080; --small-b: #ff30ff;
    --reptile-a: #5a5a5a; --reptile-b: #b8b8ff;
  }
  html, body {
    margin: 0;
    padding: 0;
    width: 1200px;
    height: 338px;
    overflow: hidden;
    background: var(--gap-white);
  }
  .sign {
    position: relative;
    width: 1200px;
    height: 338px;
    font-family: "Comfortaa", sans-serif;
    background: var(--gap-white);
  }
  .sign-board {
    position: absolute;
    left: 0; top: 0;
    width: 1200px; height: 208px;
    background: var(--sign-black);
  }
  .store-name {
    position: absolute;
    left: 0; right: 0; top: 22px;
    margin: 0;
    text-align: center;
    font-weight: 300;
    font-size: 104px;
    line-height: 1;
    letter-spacing: 1px;
    color: var(--name-orange);
  }
  .tagline-row {
    position: absolute;
    left: 23px; right: 22px; top: 150px;
    display: flex;
    align-items: center;
    gap: 16px;
  }
  .tagline-rule {
    flex: 1;
    height: 2px;
    background: var(--rule-white);
  }
  .tagline {
    margin: 0;
    font-weight: 400;
    font-size: 38px;
    line-height: 1;
    padding-bottom: 8px;
    color: var(--tagline-cyan);
    white-space: nowrap;
  }
  .category-banner {
    position: absolute;
    left: 0; top: 225px;
    width: 1200px; height: 113px;
    background: var(--sign-black);
    margin: 0;
    padding: 0;
    list-style: none;
  }
  .category {
    position: absolute;
    top: 19px;
    display: flex;
    align-items: center;
    gap: 10px;
  }
  .category-tile {
    width: 70px;
    height: 70px;
    border: 2px solid var(--label-white);
    border-radius: 12px;
    box-sizing: border-box;
  }
  .category-label {
    color: var(--label-white);
    font-weight: 300;
    font-size: 26px;
    line-height: 1.2;
  }
  .cat-fish    { left: 30px; }
  .cat-bird    { left: 244px; }
  .cat-cat     { left: 414px; }
  .cat-dog     { left: 575px; }
  .cat-small   { left: 748px; }
  .cat-reptile { left: 969px; }
  .cat-fish .category-tile    { background: linear-gradient(160deg, var(--fish-a) 45%, var(--fish-b) 55%, var(--fish-a) 80%); }
  .cat-bird .category-tile    { background: linear-gradient(160deg, var(--bird-a) 40%, var(--bird-b) 55%, var(--bird-a) 80%); }
  .cat-cat .category-tile     { background: linear-gradient(160deg, var(--cat-a) 45%, var(--cat-b) 60%, var(--cat-a) 85%); }
  .cat-dog .category-tile     { background: linear-gradient(160deg, var(--dog-a) 40%, var(--dog-b) 55%, var(--dog-a) 80%); }
  .cat-small .category-tile   { background: linear-gradient(160deg, var(--small-a) 40%, var(--small-b) 55%, var(--small-a) 80%); }
  .cat-reptile .category-tile { background: linear-gradient(160deg, var(--reptile-a) 40%, var(--reptile-b) 55%, var(--reptile-a) 80%); }
</style>
</head>
<body>
<main class="sign">
  <header class="sign-board">
    <h1 class="store-name">Tail Wag Corner</h1>
    <div class="tagline-row">
      <span class="tagline-rule"></span>
      <p class="tagline">for all your pet needs</p>
      <span class="tagline-rule"></span>
    </div>
  </header>

  <ul class="category-banner">
    <li class="category cat-fish">
      <div class="category-tile" role="img" aria-label="App-style tile with a white goldfish silhouette on orange and yellow bands"></div>
      <span class="category-label">Aquatial<br>Fish</span>
    </li>
    <li class="category cat-bird">
      <div class="category-tile" role="img" aria-label="App-style tile with a white bird silhouette on blue and cyan bands"></div>
      <span class="category-label">Birds</span>
    </li>
    <li class="category cat-cat">
      <div class="category-tile" role="img" aria-label="App-style tile with a white sitting cat silhouette on red and orange bands"></div>
      <span class="category-label">Cats</span>
    </li>
    <li class="category cat-dog">
      <div class="category-tile" role="img" aria-label="App-style tile with a white dog silhouette on dark and light green bands"></div>
      <span class="category-label">Dogs</span>
    </li>
    <li class="category cat-small">
      <div class="category-tile" role="img" aria-label="App-style tile with a white rabbit silhouette on purple and magenta bands"></div>
      <span class="category-label">Small<br>Animals</span>
    </li>
    <li class="category cat-reptile">
      <div class="category-tile" role="img" aria-label="App-style tile with a pale snake silhouette on grey and lavender bands"></div>
      <span class="category-label">Reptiles</span>
    </li>
  </ul>
</main>
</body>
</html>
```